Property developer, money partner needs business card design using logo concept provided

Our company develops residential properties, does money lends for joint ventures in property deals and finds property deals for other money partners. We have provided a basic logo for you to work from. Any graphic or logo design on the card is to communicate development and finance collaboration. Color choice is not so important for us, but color choice does need to reflect professionalism.

```html
<!DOCTYPE html>
<html lang="en">
<head>
<meta charset="utf-8">
<title>Keystone Property Partners – Business Card</title>
<link href="https://fonts.googleapis.com/css2?family=Poppins:wght@400;600&family=PT+Sans&display=swap" rel="stylesheet">
<style>
  :root{
    --bg:#333333;
    --paper:#ffffff;
    --brand-blue:#0a4a9a;
    --card-blue:#0066ae;
    --accent-red:#b01c22;
    --ink:#1a1a1a;
  }
  *{margin:0;padding:0;box-sizing:border-box}
  html,body{width:1200px;height:1000px;overflow:hidden;background:var(--bg)}
  .canvas{position:relative;width:1200px;height:1000px}
  .card{position:absolute;left:254px;width:693px;height:396px;overflow:hidden}
  .card--front{top:67px;background:var(--paper)}
  .card--back{top:537px;background:var(--card-blue)}

  .wordmark{position:absolute;font-family:"Poppins",sans-serif;font-weight:600;text-align:center;line-height:1.15}
  .wordmark__name{font-size:25px;letter-spacing:5px}
  .wordmark__sub{font-size:17px;letter-spacing:3px}
  .front .wordmark{left:40px;top:36px;color:var(--ink)}
  .acn{font-family:"Poppins",sans-serif;font-size:11px;letter-spacing:3px;margin-top:4px;text-align:center}
  .front .acn{color:var(--ink)}

  .name-marker{position:absolute;left:0;top:165px;width:25px;height:40px;background:var(--accent-red)}
  .person{position:absolute;left:39px;top:160px}
  .person__name{font-family:"Poppins",sans-serif;font-weight:600;font-size:25px;color:var(--brand-blue);line-height:1.1}
  .person__tagline{font-family:"Poppins",sans-serif;font-size:15px;color:var(--ink);margin-top:2px}

  .contacts{position:absolute;left:38px;top:230px;list-style:none;font-family:"PT Sans",sans-serif;font-size:16px;color:var(--ink);letter-spacing:.3px}
  .contacts li{display:flex;align-items:flex-start;gap:9px;line-height:20px;margin-bottom:3px}
  .contacts svg{width:13px;height:13px;margin-top:4px;fill:var(--brand-blue);flex:none}

  .mark{position:absolute;left:430px;top:60px;width:200px;height:270px;display:flex;flex-direction:column;align-items:center;justify-content:center;gap:16px}
  .mark__dot{width:150px;height:150px;border-radius:50%;background:var(--brand-blue)}
  .mark__label{font-family:"Poppins",sans-serif;font-weight:600;font-size:17px;letter-spacing:2px;color:var(--brand-blue);text-align:center;line-height:1.3}

  .band{position:absolute;bottom:0;height:13px}
  .band--blue{left:0;width:360px;background:var(--brand-blue);clip-path:polygon(0 0,100% 0,97.5% 100%,0 100%)}
  .band--red{left:356px;right:0;background:var(--accent-red);clip-path:polygon(2.3% 0,100% 0,100% 100%,0 100%)}

  .back-dot{position:absolute;left:271px;top:60px;width:150px;height:150px;border-radius:50%;background:var(--paper)}
  .back .wordmark{left:0;right:0;top:290px;color:var(--paper)}
  .back .acn{color:var(--paper)}
</style>
</head>
<body>
<div class="canvas">
  <section class="card card--front front">
    <div class="wordmark">
      <div class="wordmark__name">KEYSTONE</div>
      <div class="wordmark__sub">Property Partners</div>
      <div class="acn">A.C.N 418 302 956</div>
    </div>

    <div class="name-marker"></div>
    <div class="person">
      <div class="person__name">DANIEL REYES</div>
      <div class="person__tagline">Tagline Here</div>
    </div>

    <ul class="contacts">
      <li><svg viewBox="0 0 24 24"><path d="M12 1a8 8 0 0 0-8 8c0 6 8 14 8 14s8-8 8-14a8 8 0 0 0-8-8zm0 11a3 3 0 1 1 0-6 3 3 0 0 1 0 6z"/></svg><span>842 Linden Avenue,<br>Springfield, IL 6270</span></li>
      <li><svg viewBox="0 0 24 24"><path d="M7 1h10a2 2 0 0 1 2 2v18a2 2 0 0 1-2 2H7a2 2 0 0 1-2-2V3a2 2 0 0 1 2-2zm1 3v14h8V4zm4 15.5a1.2 1.2 0 1 0 0 2.4 1.2 1.2 0 0 0 0-2.4z"/></svg><span>(555) 214-7730</span></li>
      <li><svg viewBox="0 0 24 24"><path d="M6.6 10.8a15 15 0 0 0 6.6 6.6l2.2-2.2a1 1 0 0 1 1-.25 11 11 0 0 0 3.6.6 1 1 0 0 1 1 1V20a1 1 0 0 1-1 1A17 17 0 0 1 3 4a1 1 0 0 1 1-1h3.5a1 1 0 0 1 1 1c0 1.25.2 2.45.6 3.6a1 1 0 0 1-.25 1z"/></svg><span>(555) 214-7731</span></li>
      <li><svg viewBox="0 0 24 24"><path d="M2 4h20v16H2zm2 2v.5l8 5 8-5V6zm0 3v9h16V9l-8 5z"/></svg><span>info@keystonepartners.com</span></li>
      <li><svg viewBox="0 0 24 24"><path d="M12 1a11 11 0 1 0 0 22 11 11 0 0 0 0-22zm-1 19.9A9 9 0 0 1 3.2 10L8 15v1a2 2 0 0 0 2 2v2.9zm6.9-2.5A2 2 0 0 0 16 17h-1v-3a1 1 0 0 0-1-1H8v-2h2a1 1 0 0 0 1-1V8h2a2 2 0 0 0 2-2v-.4a9 9 0 0 1 2.9 12.8z"/></svg><span>www.keystonepartners.com</span></li>
    </ul>

    <div class="mark">
      <div class="mark__dot"></div>
      <div class="mark__label">KEYSTONE<br>Property Partners</div>
    </div>

    <div class="band band--blue"></div>
    <div class="band band--red"></div>
  </section>

  <section class="card card--back back">
    <div class="back-dot"></div>
    <div class="wordmark">
      <div class="wordmark__name">KEYSTONE</div>
      <div class="wordmark__sub">Property Partners</div>
      <div class="acn">A.C.N 418 302 956</div>
    </div>
  </section>
</div>
</body>
</html>
```